Awesome Web Design Project

must have a link to palsphere of the homepage preferably a scrolling view of our palsphere page!

We are an exciting new electrical company with a strong focus on energy efficiency and offering the latest technologies.

The design should allow easy navigation, there shouldn't be too many menus, It should look clean and sleek, Colours to consider could be green, silver/chrome, black,

The site should convey technology, efficiency and simplicity

Must be viewable on all devices, pc's, tablets, phones ie Responsive

Logo and some pics uploaded!

Industry/Entity Type

Electrical

Requirements
Must have
• must include the following pages,
about us
our services
gallery
contact us
Connect with us
Nice to have
• Would be great if the website design used a user friendly cms,
Should not have
• too many links, menus, clutter it should be clean and easy to navigate

```html
<!DOCTYPE html>
<html lang="en">
<head>
<meta charset="utf-8">
<title>Volta Lane Electrical</title>
<link href="https://fonts.googleapis.com/css2?family=Audiowide&family=Oswald:wght@300;400;600&family=Arimo:wght@400;700&display=swap" rel="stylesheet">
<style>
:root{
  --teal-dark:#0d2f38;
  --lime:#d6df22;
  --green:#4a8a00;
  --ink:#1a1a1a;
  --footer:#3f6570;
  --field:#6c949c;
  --rule:#c9cf2a;
}
*{box-sizing:border-box;margin:0;padding:0}
html,body{width:796px;height:1200px;overflow:hidden;background:#fff}
body{position:relative;font-family:"Arimo",Arial,sans-serif;color:var(--ink)}
.abs{position:absolute}

.site-header{left:0;top:0;width:796px;height:60px;background:#fff}
.brand{left:16px;top:16px;display:flex;align-items:center;gap:8px}
.brand-mark{width:26px;height:26px;background:var(--lime)}
.brand-name{font-family:"Audiowide",sans-serif;font-size:20px;color:var(--teal-dark);letter-spacing:2px}
.connect{right:14px;top:12px;display:flex;align-items:center;gap:6px;text-align:right}
.connect-text{font-family:"Oswald",sans-serif;font-weight:400;font-size:13px;line-height:14px;color:var(--teal-dark)}
.connect-box{width:34px;height:34px;background:#55707a;border-radius:4px}

.main-nav{left:0;top:60px;width:796px;height:38px;background:var(--teal-dark);border-top:3px solid var(--rule)}
.main-nav a{position:absolute;top:8px;font-family:"Audiowide",sans-serif;font-size:13px;color:var(--lime);text-decoration:none;letter-spacing:1px;transform:translateX(-50%)}
.nav-notch{left:60px;top:60px}

.hero{left:0;top:98px;width:796px;height:314px;background:linear-gradient(100deg,#3b4f66 0%,#6a7480 30%,#b9b5ad 50%,#6f7d8c 70%,#364a60 100%)}
.hero-dots{right:17px;top:387px;display:flex;gap:12px}
.hero-dots span{width:16px;height:16px;border-radius:50%;background:var(--lime)}
.hero-fade{left:0;top:412px;width:796px;height:36px;background:linear-gradient(#e6e6e6,#fff)}

.why-title{left:15px;top:462px;font-family:"Audiowide",sans-serif;font-size:26px;color:var(--teal-dark);letter-spacing:3px}
.why-text{left:15px;top:506px;width:470px;font-size:11.3px;line-height:13.6px}
.energy-title{left:14px;top:592px;font-family:"Audiowide",sans-serif;font-size:14.5px;color:var(--teal-dark);letter-spacing:2px}
.energy-graphic{left:16px;top:625px;width:236px;height:172px;background:linear-gradient(90deg,#1e7a2a 0%,#7fbf2a 45%,#e0c020 70%,#d83a1e 100%);border-radius:4px}
.energy-text{left:268px;top:615px;width:255px;font-size:11.3px;line-height:13.6px}
.energy-list{left:268px;top:697px;width:260px;list-style:none;font-size:11.3px;line-height:13.6px;color:var(--green)}
.energy-list li{position:relative;padding-left:14px}
.energy-list li::before{content:"";position:absolute;left:0;top:4px;width:7px;height:7px;border-radius:50%;background:var(--teal-dark);box-shadow:inset 0 0 0 2px var(--teal-dark)}

.service-title{left:15px;top:812px;font-family:"Oswald",sans-serif;font-weight:600;font-size:20px;color:var(--teal-dark);letter-spacing:-.3px}
.service-btn{top:862px;height:33px;background:var(--lime);border-radius:5px;font-family:"Oswald",sans-serif;font-weight:300;font-size:16px;color:var(--teal-dark);display:flex;align-items:center;justify-content:center}

.sidebar{left:597px;top:460px;width:185px}
.side-title{font-family:"Oswald",sans-serif;font-weight:300;font-size:27px;color:var(--teal-dark);line-height:32px}
.testimonial{margin-top:10px;font-size:9.8px;line-height:11.9px;padding-bottom:20px;border-bottom:1px dotted var(--rule)}
.testimonial + .testimonial{margin-top:24px}
.quote-icon{float:left;margin:0 10px 4px 0}
.testimonial .by{margin-top:8px;font-size:11.5px;color:var(--green)}
.call-label{margin-top:26px;display:flex;align-items:center;gap:6px;font-family:"Oswald",sans-serif;font-weight:300;font-size:21px;color:#4c6f78}
.call-number{font-family:"Oswald",sans-serif;font-weight:300;font-size:34px;color:var(--teal-dark);line-height:40px}

.site-footer{left:0;top:950px;width:796px;height:250px;background:var(--footer)}
.foot-title{font-family:"Oswald",sans-serif;font-weight:300;font-size:16px;color:var(--lime)}
.foot-nav{left:26px;top:24px}
.foot-nav a{display:block;font-size:10px;line-height:12px;color:#dfe8ea;text-decoration:none}
.foot-nav .foot-title{margin-bottom:10px}
.foot-rule{top:40px;height:180px;border-left:1px dotted #6c8c94}
.email-col{left:222px;top:24px;width:246px}
.field{height:21px;border-radius:11px;background:var(--field);color:#eef3f4;font-size:8.5px;font-weight:700;padding:5px 15px;margin-bottom:5px}
.field.area{height:83px;border-radius:10px}
.send{left:409px;top:196px;width:56px;height:24px;background:var(--lime);border-radius:3px;font-size:10px;font-weight:700;color:var(--teal-dark);display:flex;align-items:center;justify-content:center}
.social-col{left:608px;top:24px;width:160px}
.social-row{display:flex;gap:6px;margin-top:14px}
.social-row span{width:23px;height:23px;border-radius:50%;background:#9eb5ba}
.newsletter{margin-top:8px;font-size:8.5px;line-height:10.5px;color:#e4ecee}
.news-field{margin-top:8px;width:151px;height:20px;border-radius:10px;background:var(--field);color:#eef3f4;font-size:8.5px;padding:5px 12px}
.news-go{margin-top:9px;font-size:8.5px;font-weight:700;color:#e4ecee}
.foot-phone{margin-top:14px;display:flex;align-items:center;gap:8px;font-family:"Oswald",sans-serif;font-weight:300;font-size:22px;color:#d5e0e3}
</style>
</head>
<body>

<header class="site-header abs">
  <div class="brand abs"><span class="brand-mark"></span><span class="brand-name">VOLTA LANE</span></div>
  <div class="connect abs">
    <div class="connect-text">connect<br>with us on palsphere</div>
    <span class="connect-box"></span>
  </div>
</header>

<nav class="main-nav abs">
  <a href="#" style="left:67px">HOME</a>
  <a href="#" style="left:206px">ABOUT US</a>
  <a href="#" style="left:361px">SERVICES</a>
  <a href="#" style="left:518px">GALLERY</a>
  <a href="#" style="left:689px">CONTACT US</a>
</nav>
<svg class="nav-notch abs" width="16" height="8" viewBox="0 0 16 8"><path d="M0 0h16L8 7z" fill="#c9cf2a"/></svg>

<div class="hero abs" role="img" aria-label="Two electricians in orange hard hats wiring a distribution panel"></div>
<div class="hero-dots abs"><span></span><span></span><span></span><span></span><span></span></div>
<div class="hero-fade abs"></div>

<h1 class="why-title abs">WHY VOLTA LANE ELECTRICAL?</h1>
<p class="why-text abs">Lorem ipsum dolor sit amet, consectetur adipisicing elit, sed do eiusmod tempor incididunt ut labore et dolore magna aliqua. Ut enim ad minim veniam, quis nostrud exercitation ullamco laboris nisi ut aliquip ex ea commodo consequat. Duis aute irure dolor in reprehenderit in voluptate velit esse cillum dolore eu fugiat nulla pariatur. Excepteur sint occaecat cupidatat non proident, sunt in culpa qui officia deserunt mollit anim id est laborum.</p>

<h2 class="energy-title abs">WE USE ENERGY SAVING SOLUTIONS</h2>
<div class="energy-graphic abs" role="img" aria-label="House outline with an energy efficiency rating scale from A to G"></div>
<p class="energy-text abs">With the ever rising costs of energy, the need for each of us to make an effort to reduce our carbon foot-print and reduce our dependence on natural resources it is more important than ever for us all to "Go Green".</p>
<ul class="energy-list abs">
  <li>Energy solution cost reduction and energy conservation</li>
  <li>Lighting retro, high performance LED &amp; CPFL's</li>
  <li>Net metering &amp; off grid energy solutions</li>
  <li>Electric Car Charging Solutions</li>
</ul>

<h2 class="service-title abs">WE DO SERVICE WITH THE FOLLOWING:</h2>
<div class="service-btn abs" style="left:14px;width:92px">RESIDENTIAL</div>
<div class="service-btn abs" style="left:127px;width:92px">COMMERCIAL</div>
<div class="service-btn abs" style="left:241px;width:108px">CONSTRUCTION</div>
<div class="service-btn abs" style="left:371px;width:92px">INDUSTRIAL</div>

<aside class="sidebar abs">
  <h2 class="side-title">TESTIMONIALS</h2>
  <div class="testimonial">
    <svg class="quote-icon" width="38" height="26" viewBox="0 0 38 26"><ellipse cx="21" cy="11" rx="16" ry="9" fill="#8fb4c4"/><ellipse cx="16" cy="12" rx="15" ry="9" fill="#5f93aa"/><path d="M8 18l-3 7 9-5z" fill="#5f93aa"/></svg>
    They are very professional and thrustworthy. No need for supervision while they are installing on work. It's been a while now and my electrical linings doesn't give me any problem. I highly recommend Volta Lane electrical.
    <p class="by">by: Dana Whitfield</p>
  </div>
  <div class="testimonial">
    <svg class="quote-icon" width="38" height="26" viewBox="0 0 38 26"><ellipse cx="21" cy="11" rx="16" ry="9" fill="#8fb4c4"/><ellipse cx="16" cy="12" rx="15" ry="9" fill="#5f93aa"/><path d="M8 18l-3 7 9-5z" fill="#5f93aa"/></svg>
    They are very professional and thrustworthy. No need for supervision while they are installing on work. It's been a while now and my electrical linings doesn't give me any problem. I highly recommend Volta Lane electrical.
    <p class="by">by: Dana Whitfield</p>
  </div>
  <div class="call-label">
    <svg width="22" height="22" viewBox="0 0 22 22"><circle cx="11" cy="11" r="9.5" fill="none" stroke="#4c6f78" stroke-width="1.5"/><path d="M8 6c-1 1-1.5 2.5 0 5s3.5 4.5 5.5 5c1 .2 1.8-.5 2.2-1.2l-2-1.6-1.2.8c-1-.5-2.3-1.8-2.8-2.8l.8-1.2-1.6-2z" fill="#4c6f78"/></svg>
    CONTACT US NOW
  </div>
  <div class="call-number">0-18-55502417</div>
</aside>

<footer class="site-footer abs">
  <div class="foot-nav abs">
    <h3 class="foot-title">NAVIGATION</h3>
    <a href="#">Home</a><a href="#">About Us</a><a href="#">Services</a><a href="#">Gallery</a><a href="#">Contact Us</a>
  </div>
  <div class="foot-rule abs" style="left:147px"></div>
  <div class="email-col abs">
    <h3 class="foot-title" style="margin-bottom:10px">EMAIL US</h3>
    <div class="field">full name</div>
    <div class="field">email address</div>
    <div class="field area"></div>
  </div>
  <div class="send abs">send</div>
  <div class="foot-rule abs" style="left:545px"></div>
  <div class="social-col abs">
    <h3 class="foot-title">CONNECT WITH US</h3>
    <div class="social-row"><span></span><span></span><span></span><span></span><span></span></div>
    <p class="newsletter">subscribe to our monthly newsletter and get the best deals and discounts</p>
    <div class="news-field">enter email address</div>
    <p class="news-go">➤&nbsp; subscribe now</p>
    <div class="foot-phone">
      <svg width="22" height="22" viewBox="0 0 22 22"><circle cx="11" cy="11" r="9.5" fill="none" stroke="#d5e0e3" stroke-width="1.5"/><path d="M8 6c-1 1-1.5 2.5 0 5s3.5 4.5 5.5 5c1 .2 1.8-.5 2.2-1.2l-2-1.6-1.2.8c-1-.5-2.3-1.8-2.8-2.8l.8-1.2-1.6-2z" fill="#d5e0e3"/></svg>
      0-18-5550241
    </div>
  </div>
</footer>

</body>
</html>
```